"Dario Quillon" Business Card

Friends

My name is "Dario Quillon" and I need your help! I need a new business card for my personal use.

As background, "Dario Quillon" is actually an alias that I use when I meet women. Please use your creative skills to create an amazing business card for me to use!

In addition to including my name and contact details (see the "Must Have" section), you may wish to add a catchphrase or a title if you think it would help me :)

For background, please see:

http://www.dailybrightwire.com/2013/07/23/morton-feld-dario-quillon_n_5129847.html

Looking forward to seeing what you can do for me.

Hugs and kisses,

Dario Quillon [courtesy of PixelHarbor]

Target Market(s)

Adult women in New York City...or anywhere really.

Industry/Entity Type

Business

Requirements
Must have
• Please include the following details:

Dario Quillon
P: +1-555-3QUILLN
E: secrets@darioquillon-mail.com
Nice to have
• You might include a catchphrase, like "Quillon is my surname But you can call me Mr Smoothstep".

Or perhaps a title, like "Dario Quillon, Head of Sexy Times".

You're creative...I will leave the details to you my friends.
Should not have
• Any references to my actual name...because then, what's the point in using an alias?

```html
<!DOCTYPE html>
<html lang="en">
<head>
<meta charset="utf-8">
<title>Dario Quillon — Business Card</title>
<link rel="stylesheet" href="https://fonts.googleapis.com/css2?family=Open+Sans:wght@400;600&family=Comfortaa:wght@400&family=Aldrich&family=Marcellus&family=Tinos&display=swap">
<style>
  :root {
    --page: #ffffff;
    --card-dark: #1c1c1c;
    --card-black: #000000;
    --card-light: #ffffff;
    --ink: #111111;
    --caution: #ffd200;
    --caution-stripe: #fcea1e;
    --tagline: #9a9a9a;
  }
  html, body {
    margin: 0;
    width: 1200px;
    height: 900px;
    overflow: hidden;
    background: var(--page);
  }
  .canvas { display: block; width: 1200px; height: 900px; }
  .card-dark-face { fill: var(--card-dark); }
  .card-light-face { fill: var(--card-light); }
  .card-outline { fill: none; stroke: var(--ink); stroke-width: 1.2; }
  .card-black-face { fill: var(--card-black); }
  .band-dark { fill: var(--card-black); }
  .band-caution { fill: var(--caution-stripe); }
  .chevron { fill: var(--card-light); stroke: var(--ink); stroke-width: 5; stroke-linejoin: miter; }
  .wordmark {
    fill: var(--card-light);
    font-family: "Open Sans", sans-serif;
    font-weight: 600;
    text-anchor: middle;
    letter-spacing: 2px;
  }
  .name-line {
    fill: var(--card-light);
    font-family: "Open Sans", sans-serif;
    font-weight: 400;
    text-anchor: middle;
  }
  .rule { stroke: var(--card-light); stroke-width: 1.5; }
  .tagline {
    fill: var(--tagline);
    font-family: "Comfortaa", sans-serif;
    font-style: italic;
    text-anchor: middle;
  }
  .contact-name { fill: var(--ink); font-family: "Aldrich", sans-serif; font-size: 20px; letter-spacing: 1px; }
  .contact-phone { fill: var(--ink); font-family: "Marcellus", serif; font-size: 17px; }
  .contact-email { fill: var(--ink); font-family: "Tinos", serif; font-size: 15px; }
  .sign-frame { fill: var(--card-black); stroke: var(--card-light); stroke-width: 2; stroke-linejoin: round; }
  .sign-field { fill: var(--caution); stroke: var(--caution); stroke-width: 10; stroke-linejoin: round; }
  .stripe-block { fill: var(--caution-stripe); }
</style>
</head>
<body>
<svg class="canvas" viewBox="0 0 1200 900" xmlns="http://www.w3.org/2000/svg">
  <defs>
    <clipPath id="front-clip"><rect x="285" y="44" width="661" height="384" rx="14"/></clipPath>
    <clipPath id="back-clip"><rect x="274" y="444" width="683" height="397" rx="14"/></clipPath>
  </defs>

  <!-- Front card -->
  <g class="card card-front">
    <g clip-path="url(#front-clip)">
      <rect class="card-light-face" x="285" y="44" width="661" height="384"/>
      <rect class="card-dark-face" x="285" y="44" width="435" height="384"/>
      <rect class="band-dark" x="285" y="356" width="435" height="41"/>
      <rect class="band-caution" x="285" y="372" width="435" height="9"/>
      <polyline class="chevron" points="720,58 757,97 720,136"/>
    </g>
    <rect class="card-outline" x="285" y="44" width="661" height="384" rx="14"/>

    <text class="wordmark" x="519" y="150" font-size="58">DARIO</text>
    <text class="wordmark" x="519" y="232" font-size="58">QUILLON</text>

    <text class="name-line" x="519" y="292" font-size="19">DARIO QUILLON</text>
    <line class="rule" x1="379" y1="299" x2="662" y2="299"/>
    <text class="tagline" x="519" y="322" font-size="13">“Part time DARIO. Full time QUILLON”</text>

    <text class="contact-name" x="740" y="164">DARIO QUILLON</text>
    <text class="contact-phone" x="740" y="187">P: +1-555-3QUILLN</text>
    <text class="contact-email" x="740" y="206">E: secrets@darioquillon-mail.com</text>

    <g class="warning-sign" role="img" aria-label="Yellow warning sign with monogram and crossed bones">
      <polygon class="sign-frame" points="833,216 945,412 721,412"/>
      <polygon class="sign-field" points="833,246 922,396 744,396"/>
    </g>
  </g>

  <!-- Back card -->
  <g class="card card-back">
    <g clip-path="url(#back-clip)">
      <rect class="card-black-face" x="274" y="444" width="683" height="397"/>
      <polygon class="stripe-block" points="826,444 941,444 941,460 826,489"/>
      <polygon class="stripe-block" points="826,532 941,504 941,532 826,560"/>
      <polygon class="stripe-block" points="826,604 941,576 941,604 826,632"/>
      <polygon class="stripe-block" points="826,676 941,648 941,676 826,704"/>
      <polygon class="stripe-block" points="826,748 941,720 941,748 826,776"/>
      <polygon class="stripe-block" points="826,820 941,792 941,820 826,848"/>
    </g>

    <g class="warning-sign" role="img" aria-label="Yellow warning sign with monogram and crossed bones">
      <polygon class="sign-frame" points="615,456 730,655 500,655"/>
      <polygon class="sign-field" points="615,486 708,640 522,640"/>
    </g>

    <text class="wordmark" x="616" y="720" font-size="38">DARIO</text>
    <text class="wordmark" x="616" y="772" font-size="38">QUILLON</text>

    <text class="name-line" x="618" y="802" font-size="13">DARIO QUILLON</text>
    <line class="rule" x1="532" y1="805" x2="707" y2="805"/>
    <text class="tagline" x="618" y="820" font-size="8">“Part time DARIO. Full time QUILLON”</text>
  </g>
</svg>
</body>
</html>
```